Thornwick Holdings, Inc.
dba Marigold Lagoon - It's How Fun Is Done!
Thornwick Holdings, Inc. -
Creative Brief
Ronald Malvern
CEO
PO Box 4471 Harlow Bay, ME 04930
Rmalvern@marigoldlagoonplay.net
www.marigoldlagoonplay.net

```html
<!DOCTYPE html>
<html lang="en">
<head>
<meta charset="utf-8">
<title>Marigold Lagoon Stationery</title>
<link href="https://fonts.googleapis.com/css2?family=Open+Sans:wght@400;700&display=swap" rel="stylesheet">
<style>
  :root {
    --board: #3b3b3d;
    --board-light: #4a4a4d;
    --paper: #ffffff;
    --paper-shade: #e6e8ec;
    --blue: #1f6fc1;
    --blue-dark: #124f93;
    --red: #d8262b;
    --ink: #555a61;
    --caption: #b9bcc1;
  }
  * { box-sizing: border-box; margin: 0; padding: 0; }
  html, body { width: 1200px; height: 427px; overflow: hidden; }
  body {
    font-family: "Open Sans", Arial, sans-serif;
    background: radial-gradient(ellipse at 50% 40%, var(--board-light), var(--board) 70%);
    position: relative;
    color: var(--ink);
  }
  .piece { position: absolute; }
  .caption {
    position: absolute; font-size: 6px; color: var(--caption);
    text-align: center; white-space: nowrap;
  }
  .brand-name {
    font-family: "Open Sans", Arial, sans-serif;
    font-weight: 700; color: var(--blue); white-space: nowrap;
  }

  /* Presentation header */
  .board-brand { left: 40px; top: 50px; width: 130px; text-align: center; }
  .board-brand .mark {
    width: 50px; height: 50px; border-radius: 50%;
    background: var(--red); margin: 0 auto 6px;
  }
  .board-brand .brand-name { font-size: 14px; }
  .board-brand .concept { font-size: 7px; color: var(--caption); margin-top: 8px; }

  /* Business card */
  .business-card {
    left: 20px; top: 204px; width: 112px; height: 96px;
    background: var(--paper); box-shadow: 0 2px 6px rgba(0,0,0,.45);
    overflow: hidden;
  }
  .business-card svg { position: absolute; left: 0; top: 0; }
  .business-card .card-brand { position: absolute; left: 4px; top: 30px; width: 52px; text-align: center; }
  .business-card .card-brand .mark { width: 20px; height: 20px; border-radius: 50%; background: var(--red); margin: 0 auto 3px; }
  .business-card .card-brand .brand-name { font-size: 5.5px; }
  .business-card .contact {
    position: absolute; left: 58px; top: 14px; font-size: 3.4px; line-height: 1.55; white-space: nowrap;
  }
  .business-card .contact .name { font-weight: 700; color: var(--blue-dark); font-size: 4.5px; }
  .business-card .contact .role { margin-bottom: 14px; }
  .card-caption { left: 20px; top: 310px; width: 112px; }

  /* Letterheads */
  .letterhead {
    width: 240px; height: 298px; top: 38px;
    background: var(--paper); box-shadow: 0 2px 8px rgba(0,0,0,.45);
    overflow: hidden;
  }
  .letterhead.one { left: 232px; }
  .letterhead.two { left: 500px; }
  .letterhead svg.top-band { position: absolute; top: 0; left: 0; }
  .letterhead .head-contact {
    position: absolute; right: 12px; top: 7px; font-size: 4px; color: #ffffff;
    text-align: right; line-height: 1.5; white-space: nowrap;
  }
  .letterhead .foot-contact {
    position: absolute; left: 0; width: 100%; bottom: 6px; text-align: center;
    font-size: 3.6px; color: var(--ink); white-space: nowrap;
  }
  .letterhead .faint-brand {
    position: absolute; left: 0; width: 100%; top: 128px; text-align: center;
  }
  .letterhead .faint-brand .brand-name { font-size: 22px; color: var(--blue); opacity: .13; }
  .letterhead-caption { top: 343px; width: 240px; }
  .letterhead-caption.one { left: 232px; }
  .letterhead-caption.two { left: 500px; }

  /* Envelopes */
  .envelope { width: 276px; box-shadow: 0 2px 8px rgba(0,0,0,.45); overflow: hidden; }
  .envelope svg { position: absolute; left: 0; top: 0; }
  .envelope .env-brand { position: absolute; left: 0; width: 100%; top: 10px; text-align: center; }
  .envelope .env-brand .mark { width: 16px; height: 16px; border-radius: 50%; background: var(--paper); margin: 0 auto 2px; }
  .envelope .env-brand .brand-name { font-size: 6px; color: #ffffff; }
  .envelope .env-web { position: absolute; left: 0; width: 100%; top: 38px; text-align: center; font-size: 3.8px; color: #ffffff; }
  .envelope.back-red { left: 870px; top: 34px; height: 74px; background: var(--red); z-index: 4; }
  .envelope.back-blue { left: 870px; top: 91px; height: 89px; background: var(--blue); z-index: 3; }
  .envelope.front-white { left: 870px; top: 175px; height: 89px; background: var(--paper); z-index: 2; }
  .envelope.front-plain { left: 838px; top: 254px; height: 82px; width: 290px; background: var(--paper); z-index: 5; }
  .envelope .return {
    position: absolute; left: 10px; top: 8px; font-size: 3.8px; line-height: 1.5; white-space: nowrap;
  }
  .envelope .return .brand-name { font-size: 5.5px; }
  .envelope-caption { left: 838px; top: 343px; width: 290px; }
</style>
</head>
<body>

  <div class="piece board-brand">
    <div class="mark"></div>
    <div class="brand-name">Marigold Lagoon</div>
    <div class="concept">Stationery Concept</div>
  </div>

  <div class="piece business-card">
    <svg width="112" height="96" viewBox="0 0 112 96">
      <path d="M0 0 H112 V7 Q56 3 0 12 Z" fill="var(--blue)"/>
      <path d="M0 12 Q56 3 112 7 V10 Q56 6 0 15 Z" fill="var(--red)"/>
      <path d="M0 86 Q56 80 112 84 V96 H0 Z" fill="var(--blue)"/>
      <path d="M0 83 Q56 77 112 81 V84 Q56 80 0 86 Z" fill="var(--red)"/>
    </svg>
    <div class="card-brand">
      <div class="mark"></div>
      <div class="brand-name">Marigold Lagoon</div>
    </div>
    <div class="contact">
      <div class="name">Ronald Malvern</div>
      <div class="role">CEO</div>
      <div>PO Box 4471</div>
      <div>Harlow Bay, ME 04930</div>
      <div>Rmalvern@marigoldlagoonplay.net</div>
      <div>www.marigoldlagoonplay.net</div>
    </div>
  </div>
  <div class="caption card-caption">Business Card</div>

  <div class="piece letterhead one">
    <svg class="top-band" width="240" height="40" viewBox="0 0 240 40">
      <path d="M0 0 H240 V22 Q110 17 0 31 Z" fill="var(--blue)"/>
      <path d="M0 31 Q110 17 240 22 V26 Q110 22 0 36 Z" fill="var(--red)"/>
    </svg>
    <div class="head-contact">PO Box 4471 Harlow Bay, ME 04930<br>www.marigoldlagoonplay.net</div>
    <div class="faint-brand"><span class="brand-name">Marigold Lagoon</span></div>
  </div>

  <div class="piece letterhead two">
    <svg class="top-band" width="240" height="40" viewBox="0 0 240 40">
      <path d="M0 0 H240 V22 Q110 17 0 31 Z" fill="var(--blue)"/>
      <path d="M0 31 Q110 17 240 22 V26 Q110 22 0 36 Z" fill="var(--red)"/>
    </svg>
    <div class="faint-brand"><span class="brand-name">Marigold Lagoon</span></div>
    <div class="foot-contact">PO Box 4471 Harlow Bay, ME 04930 &nbsp; Rmalvern@marigoldlagoonplay.net &nbsp; www.marigoldlagoonplay.net</div>
  </div>

  <div class="caption letterhead-caption one">Letterhead Option 1</div>
  <div class="caption letterhead-caption two">Letterhead Option 2</div>

  <div class="piece envelope back-red">
    <svg width="276" height="74" viewBox="0 0 276 74">
      <path d="M0 60 Q138 50 276 62 V74 H0 Z" fill="var(--paper)"/>
    </svg>
    <div class="env-brand"><div class="mark"></div><div class="brand-name">Marigold Lagoon</div></div>
    <div class="env-web">www.marigoldlagoonplay.net</div>
  </div>

  <div class="piece envelope back-blue">
    <svg width="276" height="89" viewBox="0 0 276 89">
      <path d="M0 0 L138 40 L276 0" fill="none" stroke="var(--blue-dark)" stroke-width="1"/>
      <path d="M0 76 Q138 64 276 78 V89 H0 Z" fill="var(--paper)"/>
    </svg>
    <div class="env-brand" style="top:36px;"><div class="brand-name">Marigold Lagoon</div></div>
  </div>

  <div class="piece envelope front-white">
    <svg width="276" height="89" viewBox="0 0 276 89">
      <path d="M0 0 L138 40 L276 0" fill="none" stroke="var(--paper-shade)" stroke-width="1.2"/>
    </svg>
  </div>

  <div class="piece envelope front-plain">
    <svg width="290" height="82" viewBox="0 0 290 82">
      <path d="M0 68 Q145 58 290 70 V82 H0 Z" fill="var(--blue)"/>
      <path d="M0 64 Q145 54 290 66 V70 Q145 58 0 68 Z" fill="var(--red)"/>
    </svg>
    <div class="return">
      <div class="brand-name">Marigold Lagoon</div>
      <div>PO Box 4471</div>
      <div>Harlow Bay, ME 04930</div>
    </div>
  </div>
  <div class="caption envelope-caption">Envelopes Front &amp; Back</div>

</body>
</html>
```